Summer Drinks Flyer for Coffee Shop

We are a coffee shop in London and would like to have a cool and nice flyer for our summer drinks (juices and frozen drink) flyer - see on the attached file for the list

Attached you can find an "attempt" - please note that I would no necessary need the image below.

I also attache our new logo.

thank you

Industry/Entity Type

Coffee Shop

```html
<!DOCTYPE html>
<html lang="en">
<head>
<meta charset="utf-8">
<title>New Summer Drinks Menu – solmare</title>
<link rel="stylesheet" href="https://fonts.googleapis.com/css2?family=Quicksand:wght@500;700&family=Kaushan+Script&family=Caveat:wght@600&display=swap">
<style>
  :root {
    --gold: #bc8f2f;
    --white: #ffffff;
    --blue: #2ba6de;
    --pink: #e08fc1;
    --red: #e4212b;
    --orange: #f2a530;
    --brown: #a27c52;
    --grey: #8c8c8c;
    --green: #3fb04a;
    --lime: #8bc53f;
    --yellow: #f5e31a;
    --banana: #f5a623;
  }
  * { box-sizing: border-box; margin: 0; padding: 0; }
  html, body {
    width: 1200px; height: 1000px; overflow: hidden;
    background: var(--white);
  }
  .canvas { position: relative; width: 1200px; height: 1000px; }

  .menu {
    position: absolute; top: 122px; width: 536px; height: 756px;
    font-family: "Quicksand", sans-serif;
  }
  .menu--gold {
    left: 44px; background: var(--gold);
    --title: var(--white); --note: var(--white); --brand: var(--white);
    --c1-head: var(--white); --c1-item: var(--white);
    --c2-head: var(--white); --c2-item: var(--white);
    --c3-head: var(--white); --c3-item: var(--white);
    --illo-fill: rgba(255,255,255,0.22);
    --glass: var(--illo-fill); --apple: var(--illo-fill); --berry: var(--illo-fill);
    --pineapple: var(--illo-fill); --banana-fill: var(--illo-fill);
  }
  .menu--light {
    left: 619px;
    --title: var(--gold); --note: var(--green); --brand: var(--gold);
    --c1-head: var(--blue); --c1-item: var(--pink);
    --c2-head: var(--red); --c2-item: var(--orange);
    --c3-head: var(--brown); --c3-item: var(--grey);
    --glass: rgba(139,197,63,0.25); --apple: rgba(228,33,43,0.22);
    --berry: rgba(224,143,193,0.3); --pineapple: rgba(245,227,26,0.4);
    --banana-fill: rgba(245,166,35,0.3);
  }

  .illo { position: absolute; border-radius: 40% 40% 30% 30%; }
  .illo--glass { left: 28px; top: 10px; width: 92px; height: 204px; background: var(--glass); border-radius: 12px 12px 30px 30px; }
  .illo--apple { left: 418px; top: 21px; width: 90px; height: 112px; background: var(--apple); border-radius: 50%; }
  .illo--berries { left: 424px; top: 130px; width: 104px; height: 84px; background: var(--berry); border-radius: 45%; }
  .illo--pineapple { left: 18px; top: 634px; width: 66px; height: 114px; background: var(--pineapple); border-radius: 45% 45% 50% 50%; }
  .illo--banana { left: 88px; top: 674px; width: 92px; height: 68px; background: var(--banana-fill); border-radius: 10% 60% 50% 50%; }

  .title {
    position: absolute; left: 134px; top: 72px;
    font-family: "Kaushan Script", cursive;
    font-weight: 400; font-size: 49px; line-height: 52px;
    color: var(--title);
  }

  .section { position: absolute; left: 23px; width: 493px; }
  .section--frozen { top: 232px; --head: var(--c1-head); --item: var(--c1-item); }
  .section--juices { top: 345px; --head: var(--c2-head); --item: var(--c2-item); }
  .section--iced { top: 518px; --head: var(--c3-head); --item: var(--c3-item); }

  .section__head {
    display: flex; justify-content: space-between;
    font-weight: 700; font-size: 27px; line-height: 32px;
    letter-spacing: 1.6px; color: var(--head);
  }
  .section__price { letter-spacing: 0.5px; }
  .section__items {
    list-style: none; margin-top: 2px;
    font-weight: 500; font-size: 20.5px; line-height: 25.2px;
    letter-spacing: 1.3px; color: var(--item);
  }

  .note {
    position: absolute; width: 200px; text-align: center;
    font-family: "Caveat", cursive; font-weight: 600;
    font-size: 23px; line-height: 26px; color: var(--note);
    transform: rotate(-13deg);
  }
  .note--mint { left: 240px; top: 404px; }
  .note--syrup { left: 240px; top: 552px; }

  .brand {
    position: absolute; left: 344px; top: 676px; width: 164px;
    display: flex; flex-direction: column; align-items: center; gap: 6px;
    color: var(--brand);
  }
  .brand__dot { width: 22px; height: 22px; border-radius: 50%; background: var(--brand); }
  .brand__name { font-family: "Quicksand", sans-serif; font-weight: 500; font-size: 40px; line-height: 40px; }
</style>
</head>
<body>
<main class="canvas">
  <section class="menu menu--gold">
    <div class="illo illo--glass" role="img" aria-label="Line illustration of a smoothie glass with a straw"></div>
    <div class="illo illo--apple" role="img" aria-label="Line illustration of an apple"></div>
    <div class="illo illo--berries" role="img" aria-label="Line illustration of two strawberries"></div>
    <h1 class="title">New Summer<br>Drinks Menu</h1>

    <div class="section section--frozen">
      <h2 class="section__head"><span>Frozen Fruit Drinks</span><span class="section__price">£2.95</span></h2>
      <ul class="section__items"><li>Strawberry &amp; Banana</li><li>Pineapple, Mango &amp; Banana</li></ul>
    </div>
    <div class="section section--juices">
      <h2 class="section__head"><span>Fruit Juices</span><span class="section__price">£2.95</span></h2>
      <ul class="section__items"><li>Orange &amp; Carrot</li><li>Orange &amp; Pineapple</li><li>Pineapple &amp; Apple</li><li>Apple &amp; Kiwi</li><li>Carrot &amp; Ginger</li></ul>
    </div>
    <p class="note note--mint">Add Mint or Ginger<br>for Free!</p>
    <div class="section section--iced">
      <h2 class="section__head"><span>Iced Coffees</span><span class="section__price">£2.45</span></h2>
      <ul class="section__items"><li>Iced Coffee</li><li>Iced Latte</li><li>Iced Chocolate Drink</li></ul>
    </div>
    <p class="note note--syrup">Add Syrup Shot<br>for 10p</p>

    <div class="illo illo--pineapple" role="img" aria-label="Line illustration of a pineapple"></div>
    <div class="illo illo--banana" role="img" aria-label="Line illustration of a banana"></div>
    <div class="brand"><span class="brand__dot"></span><span class="brand__name">solmare</span></div>
  </section>

  <section class="menu menu--light">
    <div class="illo illo--glass" role="img" aria-label="Green line illustration of a smoothie glass with a straw"></div>
    <div class="illo illo--apple" role="img" aria-label="Red line illustration of an apple"></div>
    <div class="illo illo--berries" role="img" aria-label="Pink line illustration of two strawberries"></div>
    <h1 class="title">New Summer<br>Drinks Menu</h1>

    <div class="section section--frozen">
      <h2 class="section__head"><span>Frozen Fruit Drinks</span><span class="section__price">£2.95</span></h2>
      <ul class="section__items"><li>Strawberry &amp; Banana</li><li>Pineapple, Mango &amp; Banana</li></ul>
    </div>
    <div class="section section--juices">
      <h2 class="section__head"><span>Fruit Juices</span><span class="section__price">£2.95</span></h2>
      <ul class="section__items"><li>Orange &amp; Carrot</li><li>Orange &amp; Pineapple</li><li>Pineapple &amp; Apple</li><li>Apple &amp; Kiwi</li><li>Carrot &amp; Ginger</li></ul>
    </div>
    <p class="note note--mint">Add Mint or Ginger<br>for Free!</p>
    <div class="section section--iced">
      <h2 class="section__head"><span>Iced Coffees</span><span class="section__price">£2.45</span></h2>
      <ul class="section__items"><li>Iced Coffee</li><li>Iced Latte</li><li>Iced Chocolate Drink</li></ul>
    </div>
    <p class="note note--syrup">Add Syrup Shot<br>for 10p</p>

    <div class="illo illo--pineapple" role="img" aria-label="Yellow line illustration of a pineapple"></div>
    <div class="illo illo--banana" role="img" aria-label="Orange line illustration of a banana"></div>
    <div class="brand"><span class="brand__dot"></span><span class="brand__name">solmare</span></div>
  </section>
</main>
</body>
</html>
```